Need brochure designed for my marijuana web startup.

PLEASE READ THE INSTRUCTIONS THOROUGHLY. YOUR SUBMISSION WILL BE REJECTED IF THEY ARE NOT FOLLOWED.

may lead to other immediate design work, such as flyers, postcards, banners, etc.

I need a PRINT trifold brochure or pamphlet designed for my company, Plainleaf.net. We are a bootstrapped medical marijuana search engine, locator, listing service and community.

I will be selling my web product and services to medical marijuana dispensaries and would like to quickly demonstrate why my service is better over my competitors..

I have drafted a (poorly designed) brochure that talks about all the points I wanted to hit on. I'd also like to add our 3 pricing plans in the brochure, but if there isn't any room, i'm fine with that.

I received some design guidelines from a branding consulting firm, so the designs must adhere to those rules. These guidelines are attached as a pdf. These guidelines include things like minimum clear space for the logo, primary and secondary colors, and font style.

Target Market(s)

marijuana dispensaries

Industry/Entity Type

Startup

Font styles to use
Other font styles liked:
• gotham rounded

Colors
9bcb3b

Requirements
Must have
• follow the design guidelines attached, including colors used! font files are attached.
• this is a PRINT brochure request. can be trifold, or 1 fold.
• The TEXT or "COPY" is all included in the brochure.doc attachment. There is additional stats in the "Nice to Haves" section that you may or may not include. up to you. Pricing info is included as an attachment called "Pricing Plan"
• please, keep it simple!
Nice to have
• some graphics.
• pricing plan.
• some statistics that may be interesting to help highlight how special unique items that are hard to find can be easily found with my service:
• From a sample of 2,594 active listings, there are over 153,000 items being sold:
• 12,900 marijuana related accessories (bongs, pipes, clothes, vapor pens, etc.)
• 20,300 concentrates
• 40,400 edibles
• 52,400 flowers (bud and shakes)
• 21,500 other - oral (pills, sprays), topical (lotions, soaps), seeds, oils
• 5,500 pre-rolled marijuana cigarettes (joints, blunts)
• of the 153,000 items, there are:
• 17,750+ hybrid items
• 27,100+ indica items
• 15,000+ sativa items
• in the world of edibles, there are:
• 200+ gluten free items
• 300+ sugar free items
• doses in edibles range from .3mg to 2,353mg (i.e. olive oil) the recommended dosage is 5-10mg
• 2,900+ items of 100mg edibles make it the most common dose offered on the market.
• there are over 4,000 items that are high in CBD (the medicinal chemical of weed).
Should not have
• no photos.

```html
<!DOCTYPE html>
<html lang="en">
<head>
<meta charset="utf-8">
<title>Plainleaf – Pricing Plans</title>
<link href="https://fonts.googleapis.com/css2?family=Arimo:wght@400;700&family=Open+Sans:wght@600;700&family=Quicksand:wght@500&display=swap" rel="stylesheet">
<style>
  :root{
    --backdrop:#0b0b0b;
    --page:#ffffff;
    --brand:#4a9a3c;
    --accent:#8cc63f;
    --band:#7dc67a;
    --card-top:#3a3a3a;
    --card-bottom:#1c1c1c;
    --trial:#e4e86a;
    --feature-bg:#efefef;
    --feature-text:#3a3a3a;
    --rule:#d4d4d4;
    --wash:#eef5de;
  }
  *{margin:0;padding:0;box-sizing:border-box}
  html,body{width:1200px;height:1000px;overflow:hidden;background:var(--backdrop)}
  .canvas{position:relative;width:1200px;height:1000px}
  .brochure{position:absolute;left:278px;top:62px;width:638px;height:896px;background:var(--page);overflow:hidden}
  .leaf-wash{position:absolute;left:0;width:638px;
    background:linear-gradient(160deg,var(--wash) 0%,#fbfdf6 40%,var(--wash) 70%,#ffffff 100%)}
  .leaf-wash--top{top:0;height:56px}
  .leaf-wash--body{top:206px;height:640px;opacity:.7}
  .masthead{position:absolute;left:0;top:56px;width:638px;height:150px;background:var(--page);
    display:flex;align-items:center;justify-content:center;gap:22px}
  .masthead__mark{width:46px;height:46px;border-radius:50%;background:var(--brand)}
  .masthead__name{font-family:"Quicksand",sans-serif;font-weight:500;font-size:72px;color:var(--brand);letter-spacing:1px}

  .plan{position:absolute;top:237px;width:182px;height:198px;border-radius:5px;
    background:linear-gradient(180deg,var(--card-top),var(--card-bottom));color:#fff;font-family:"Arimo",sans-serif}
  .plan__head{height:32px;border-bottom:1px solid #555;display:flex;align-items:center;justify-content:space-between;padding:0 7px 0 13px}
  .plan__name{font-size:13px}
  .plan__subscribe{background:var(--accent);color:#fff;font-size:10px;font-weight:700;border-radius:3px;padding:4px 9px}
  .plan__price{position:absolute;top:52px;left:0;width:100%;text-align:center;font-size:60px;line-height:1}
  .plan__price sup{font-size:20px;vertical-align:top;position:relative;top:6px}
  .plan__price small{font-size:8px}
  .plan__trial{position:absolute;top:139px;width:100%;text-align:center;font-size:10px;color:var(--trial)}
  .plan__pitch{position:absolute;top:167px;left:17px;right:10px;font-size:7px;line-height:10px;color:#ddd}

  .features{position:absolute;width:182px;list-style:none;font-family:"Arimo",sans-serif;font-weight:700;
    font-size:7.5px;letter-spacing:.3px;color:var(--feature-text);text-transform:uppercase}
  .features--core{top:449px;height:90px;background:var(--feature-bg);border-radius:4px;padding:1px 7px}
  .features--extra{top:555px;padding:0 7px}
  .features--plus{top:681px;left:432px;width:182px;border:1px solid var(--rule);border-radius:4px;padding:2px 7px}
  .features li{height:22px;display:flex;align-items:center;gap:6px;border-bottom:1px solid var(--rule)}
  .features li:last-child{border-bottom:none}
  .features svg{width:8px;height:8px;flex:none;fill:#333}
  .features--plus svg{fill:var(--brand)}
  .features--plus li{border-bottom-color:#c7c7c7}

  .placeholder-frame{position:absolute;left:20px;top:560px}
  .cta{position:absolute;left:0;bottom:0;width:638px;height:49px;background:var(--band);
    font-family:"Open Sans",sans-serif;font-weight:600;font-size:40px;color:#fff;text-align:center;line-height:49px}
</style>
</head>
<body>
<div class="canvas">
  <main class="brochure">
    <div class="leaf-wash leaf-wash--top" role="img" aria-label="Soft light green leaf pattern"></div>
    <div class="leaf-wash leaf-wash--body" role="img" aria-label="Faint light green leaf pattern"></div>

    <header class="masthead">
      <span class="masthead__mark"></span>
      <span class="masthead__name">plainleaf</span>
    </header>

    <section class="plan" style="left:25px">
      <div class="plan__head"><span class="plan__name">starter</span><span class="plan__subscribe">subscribe</span></div>
      <div class="plan__price"><sup>$</sup>19<small>/MO</small></div>
      <div class="plan__trial">1 month free trial</div>
      <p class="plan__pitch">try plainleaf for a month, and see if we can help you sell an extra gram</p>
    </section>
    <section class="plan" style="left:228px">
      <div class="plan__head"><span class="plan__name">basic</span><span class="plan__subscribe">subscribe</span></div>
      <div class="plan__price"><sup>$</sup>79<small>/MO</small></div>
      <div class="plan__trial">1 month free trial</div>
      <p class="plan__pitch">try plainleaf for a month, and see if we can help you sell an extra quarter ounce</p>
    </section>
    <section class="plan" style="left:432px">
      <div class="plan__head"><span class="plan__name">plus</span><span class="plan__subscribe">subscribe</span></div>
      <div class="plan__price"><sup>$</sup>349<small>/MO</small></div>
      <div class="plan__trial">1 month free trial</div>
      <p class="plan__pitch">try plainleaf for a month, and see if we can help you sell an extra ounce</p>
    </section>

    <ul class="features features--core" style="left:25px">
      <li><svg viewBox="0 0 8 8"><path d="M4 0L8 4H7V8H5V5H3V8H1V4H0Z"/></svg>Address, contact, hours</li>
      <li><svg viewBox="0 0 8 8"><path d="M0 3H2V8H0ZM3 3L5 0H6V3H8V6L7 8H3Z"/></svg>Ratings &amp; reviews</li>
      <li><svg viewBox="0 0 8 8"><circle cx="4" cy="2" r="2"/><path d="M0 8C0 5 2 4.5 4 4.5S8 5 8 8Z"/></svg>Member alerts</li>
      <li><svg viewBox="0 0 8 8"><path d="M0 0H2V2H0ZM3 0H8V2H3ZM0 3H2V5H0ZM3 3H8V5H3ZM0 6H2V8H0ZM3 6H8V8H3Z"/></svg>Store menu (6 categories)</li>
    </ul>
    <ul class="features features--core" style="left:228px">
      <li><svg viewBox="0 0 8 8"><path d="M4 0L8 4H7V8H5V5H3V8H1V4H0Z"/></svg>Address, contact, hours</li>
      <li><svg viewBox="0 0 8 8"><path d="M0 3H2V8H0ZM3 3L5 0H6V3H8V6L7 8H3Z"/></svg>Ratings &amp; reviews</li>
      <li><svg viewBox="0 0 8 8"><circle cx="4" cy="2" r="2"/><path d="M0 8C0 5 2 4.5 4 4.5S8 5 8 8Z"/></svg>Member alerts</li>
      <li><svg viewBox="0 0 8 8"><path d="M0 0H2V2H0ZM3 0H8V2H3ZM0 3H2V5H0ZM3 3H8V5H3ZM0 6H2V8H0ZM3 6H8V8H3Z"/></svg>Store menu (6 categories)</li>
    </ul>
    <ul class="features features--core" style="left:432px">
      <li><svg viewBox="0 0 8 8"><path d="M4 0L8 4H7V8H5V5H3V8H1V4H0Z"/></svg>Address, contact, hours</li>
      <li><svg viewBox="0 0 8 8"><path d="M0 3H2V8H0ZM3 3L5 0H6V3H8V6L7 8H3Z"/></svg>Ratings &amp; reviews</li>
      <li><svg viewBox="0 0 8 8"><circle cx="4" cy="2" r="2"/><path d="M0 8C0 5 2 4.5 4 4.5S8 5 8 8Z"/></svg>Member alerts</li>
      <li><svg viewBox="0 0 8 8"><path d="M0 0H2V2H0ZM3 0H8V2H3ZM0 3H2V5H0ZM3 3H8V5H3ZM0 6H2V8H0ZM3 6H8V8H3Z"/></svg>Store menu (6 categories)</li>
    </ul>

    <ul class="features features--extra" style="left:228px">
      <li><svg viewBox="0 0 8 8"><path d="M0 0H8V6H3L1 8V6H0Z"/></svg>Promotional tagline</li>
      <li><svg viewBox="0 0 8 8"><path d="M6 0L8 2L2 8H0V6Z"/></svg>Business description</li>
      <li><svg viewBox="0 0 8 8"><circle cx="4" cy="4" r="3.2"/><circle cx="4" cy="4" r="1.2" fill="#fff"/></svg>Dispensary features</li>
      <li><svg viewBox="0 0 8 8"><path d="M0 2H2L3 1H5L6 2H8V7H0Z"/><circle cx="4" cy="4.5" r="1.4" fill="#fff"/></svg>Image hosting</li>
      <li><svg viewBox="0 0 8 8"><path d="M0 3H2L7 0V8L2 5H0Z"/></svg>Announcements</li>
    </ul>
    <ul class="features features--extra" style="left:432px">
      <li><svg viewBox="0 0 8 8"><path d="M0 0H8V6H3L1 8V6H0Z"/></svg>Promotional tagline</li>
      <li><svg viewBox="0 0 8 8"><path d="M6 0L8 2L2 8H0V6Z"/></svg>Business description</li>
      <li><svg viewBox="0 0 8 8"><circle cx="4" cy="4" r="3.2"/><circle cx="4" cy="4" r="1.2" fill="#fff"/></svg>Dispensary features</li>
      <li><svg viewBox="0 0 8 8"><path d="M0 2H2L3 1H5L6 2H8V7H0Z"/><circle cx="4" cy="4.5" r="1.4" fill="#fff"/></svg>Image hosting</li>
      <li><svg viewBox="0 0 8 8"><path d="M0 3H2L7 0V8L2 5H0Z"/></svg>Announcements</li>
    </ul>

    <ul class="features features--plus">
      <li><svg viewBox="0 0 8 8"><path d="M0 0H3V3H0ZM5 0H8V3H5ZM0 5H3V8H0ZM5 5H8V8H5Z"/></svg>Daily specials</li>
      <li><svg viewBox="0 0 8 8"><path d="M0 0H4L8 4L4 8L0 4Z"/></svg>First time patient deals</li>
      <li><svg viewBox="0 0 8 8"><path d="M4 0A3 3 0 0 1 7 3C7 5 4 8 4 8S1 5 1 3A3 3 0 0 1 4 0Z"/></svg>Search optimization</li>
      <li><svg viewBox="0 0 8 8"><path d="M3 0H5V3H8V5H5V8H3V5H0V3H3Z"/></svg>Expanded item view</li>
      <li><svg viewBox="0 0 8 8"><path d="M3.3 0H4.7V1.2C6 1.4 7 2 7 3H5.6C5.5 2.6 5 2.4 4 2.4S2.6 2.7 2.6 3.1 3 3.6 4.3 3.8C6.2 4.1 7.2 4.6 7.2 5.8 7.2 6.8 6.2 7.4 4.7 7.5V8H3.3V7.5C1.9 7.3 1 6.6 1 5.6H2.4C2.5 6 3 6.3 4 6.3S5.6 6 5.6 5.7 5.1 5.2 3.8 5C2 4.7 1.1 4.2 1.1 3.1 1.1 2.1 2 1.4 3.3 1.2Z"/></svg>Item promotions</li>
      <li><svg viewBox="0 0 8 8"><path d="M5.5 0A2.5 2.5 0 0 0 3.2 3.4L0 6.6 1.4 8 4.6 4.8A2.5 2.5 0 0 0 8 2.5L6.5 3 5 1.5 5.5 0Z"/></svg>Advanced customer support</li>
    </ul>

    <svg class="placeholder-frame" width="370" height="262" viewBox="0 0 370 262" aria-hidden="true">
      <polygon points="0,6 165,6 165,124 360,124 360,262 0,262" fill="#ffffff"/>
      <polyline points="0,6 165,6 165,124 360,124 360,262" fill="none" stroke="var(--band)" stroke-width="7"/>
    </svg>

    <div class="cta">Take your plan now</div>
  </main>
</div>
</body>
</html>
```